Tamarind Crest Management - Business Cards

I need business cards. My current logo was designed by a designer at this site and I very much like and am happy with the results. I would like a business card that is trendy, unique, current yet professional. I deal with high net worth clients daily

Target Market(s)

Out of state investors looking to get into the rental market in Ohio

Industry/Entity Type

Property Management, Consulting

Contact Information for Business Card

Name, Title (Chief Financial Officer) office phone number (347) 681-9072 website address tamcrestmgmt.example

Font styles to use
Sans Serif

Colors
0054AA
0677BA
7BADD7
CADEEF
E8F1F8
0094D4
00A9DD
6FCCEA
C7EBF8
E9F6FB
00AB8E
00BBA5
67D7C9
C6EFE9
E9F9F6

```html
<!DOCTYPE html>
<html lang="en">
<head>
<meta charset="utf-8">
<title>Tamarind Crest Management – Business Cards</title>
<link rel="stylesheet" href="https://fonts.googleapis.com/css2?family=Montserrat:wght@400;500;700&display=swap">
<style>
  :root {
    --navy: #24355f;
    --navy-deep: #1f2d52;
    --red: #d2262f;
    --white: #ffffff;
    --ink: #222428;
    --stage: #3b3c3f;
  }
  * { box-sizing: border-box; margin: 0; padding: 0; }
  html, body { width: 1200px; height: 1200px; overflow: hidden; }
  body {
    background: var(--stage);
    font-family: "Montserrat", sans-serif;
    position: relative;
  }
  .card {
    position: absolute;
    left: 180px;
    width: 840px;
    height: 480px;
    border-radius: 34px;
    overflow: hidden;
    box-shadow: 0 14px 30px rgba(0,0,0,0.35);
  }
  .card-front { top: 80px; background: var(--white); }
  .card-back {
    top: 640px;
    background: linear-gradient(160deg, #2a3c68 0%, var(--navy-deep) 100%);
    display: flex; align-items: center; justify-content: center;
  }
  .wordmark {
    font-weight: 700;
    text-transform: uppercase;
    text-align: center;
    line-height: 1.05;
  }
  .front-wordmark {
    position: absolute;
    left: 200px; top: 70px; width: 280px;
    color: var(--navy);
    font-size: 30px;
  }
  .back-wordmark {
    color: var(--white);
    font-size: 52px;
  }
  .accent-rule {
    position: absolute;
    left: 400px; top: 290px;
    width: 400px; height: 2px;
    background: var(--red);
  }
  .identity {
    position: absolute;
    left: 70px; top: 250px;
  }
  .person-name {
    color: var(--red);
    font-weight: 700;
    font-size: 40px;
    letter-spacing: 0.5px;
    line-height: 1;
  }
  .person-title {
    color: var(--ink);
    font-weight: 500;
    font-size: 20px;
    letter-spacing: 0.6px;
    margin-top: 6px;
  }
  .identity-rule {
    width: 310px; height: 2px;
    background: var(--red);
    margin: 14px 0 16px 10px;
  }
  .contact-list { list-style: none; margin-left: 18px; }
  .contact-item {
    display: flex; align-items: center; gap: 14px;
    color: var(--ink);
    font-size: 26px;
    letter-spacing: 0.4px;
    margin-bottom: 10px;
  }
  .contact-icon { width: 26px; height: 26px; flex: none; }
  .base-bands {
    position: absolute; left: 0; bottom: 0;
    width: 840px; height: 70px;
  }
</style>
</head>
<body>
  <section class="card card-front" aria-label="Business card front">
    <div class="wordmark front-wordmark">Tamarind Crest Management</div>
    <div class="accent-rule"></div>
    <div class="identity">
      <p class="person-name">FULL NAME</p>
      <p class="person-title">CHIEF FINANCIAL OFFICER</p>
      <div class="identity-rule"></div>
      <ul class="contact-list">
        <li class="contact-item">
          <svg class="contact-icon" viewBox="0 0 24 24" aria-hidden="true"><path fill="#d2262f" d="M6.6 10.8a15.1 15.1 0 0 0 6.6 6.6l2.2-2.2c.3-.3.7-.4 1-.2 1.1.4 2.3.6 3.6.6.6 0 1 .4 1 1V20c0 .6-.4 1-1 1A17 17 0 0 1 3 4c0-.6.4-1 1-1h3.5c.6 0 1 .4 1 1 0 1.3.2 2.5.6 3.6.1.3 0 .7-.2 1z"/></svg>
          <span>(347) 681-9072</span>
        </li>
        <li class="contact-item">
          <svg class="contact-icon" viewBox="0 0 24 24" aria-hidden="true" fill="none" stroke="#d2262f" stroke-width="2"><circle cx="12" cy="12" r="10"/><ellipse cx="12" cy="12" rx="4.5" ry="10"/><path d="M2 12h20M4 7h16M4 17h16"/></svg>
          <span>tamcrestmgmt.example</span>
        </li>
      </ul>
    </div>
    <svg class="base-bands" viewBox="0 0 840 70" aria-hidden="true">
      <polygon points="0,48 622,8 614,70 0,70" fill="#d2262f"/>
      <polygon points="640,6 840,-6 840,70 630,70" fill="#24355f"/>
    </svg>
  </section>

  <section class="card card-back" aria-label="Business card back">
    <div class="wordmark back-wordmark">Tamarind Crest<br>Management</div>
  </section>
</body>
</html>
```